Post Lockdown Ortho Special

We are running a special for (Ortho) Braces/Clear Aligner (Quorventa), till July 31st 2020. Up to $2,000 off with free Consultation and Xrays.

We need a ad to run in different formats.

Maybe something with: what better time to get braces when you have to wear a mask all the time.

Trying to rebuild our business and get people in for free consultations.

```html
<!DOCTYPE html>
<html lang="en">
<head>
<meta charset="utf-8">
<title>Post Lockdown Ortho Special</title>
<link href="https://fonts.googleapis.com/css2?family=Bebas+Neue&family=Poppins:wght@500;600;700&display=swap" rel="stylesheet">
<style>
  :root {
    --purple: #5e3a93;
    --purple-soft: #7450a6;
    --ink: #242424;
    --white: #ffffff;
    --bg-top: #ffffff;
    --bg-bottom: #e9e9ef;
    --silver: #b9b9bf;
  }
  * { margin: 0; padding: 0; box-sizing: border-box; }
  html, body { width: 1200px; height: 1200px; overflow: hidden; }
  body { font-family: "Poppins", sans-serif; }
  .ad {
    position: relative;
    width: 1200px;
    height: 1200px;
    overflow: hidden;
    background: linear-gradient(180deg, var(--bg-top) 0%, var(--bg-top) 50%, var(--bg-bottom) 100%);
  }
  .shapes { position: absolute; inset: 0; }
  .brand {
    position: absolute;
    left: 840px;
    top: 78px;
    display: flex;
    align-items: center;
    gap: 16px;
    color: var(--purple);
    font-weight: 600;
  }
  .brand-dot {
    width: 64px; height: 64px; border-radius: 50%;
    background: var(--purple-soft);
  }
  .brand-name { font-size: 30px; line-height: 1.05; letter-spacing: 1px; }
  .brand-name small { display: block; font-size: 12px; letter-spacing: 4px; margin-top: 6px; }
  .headline {
    position: absolute;
    right: 42px;
    top: 276px;
    text-align: right;
    font-family: "Bebas Neue", sans-serif;
    font-size: 118px;
    line-height: 116px;
    letter-spacing: 14px;
    margin-right: -14px;
  }
  .headline .accent { color: var(--purple-soft); }
  .headline .dark { color: var(--ink); }
  .rule {
    position: absolute;
    left: 600px; top: 645px;
    width: 600px; height: 4px;
    background: var(--ink);
  }
  .tagline {
    position: absolute;
    left: 0; top: 696px;
    width: 1200px;
    text-align: center;
    font-weight: 700;
    font-size: 40px;
    line-height: 54px;
    letter-spacing: 4.5px;
    color: var(--ink);
  }
  .tagline .hl { color: var(--purple-soft); }
  .date-text {
    position: absolute;
    left: 740px; top: 868px;
    width: 440px;
    text-align: center;
    font-size: 58px;
    font-weight: 500;
    color: var(--white);
  }
  .offer-text {
    position: absolute;
    left: 306px; top: 1010px;
    font-size: 41px;
    font-weight: 500;
    color: var(--white);
  }
  .badge-text {
    position: absolute;
    left: 58px; top: 985px;
    width: 200px;
    text-align: center;
    color: var(--white);
    font-weight: 500;
    line-height: 1;
  }
  .badge-text .small { font-size: 24px; display: block; }
  .badge-text .big { font-size: 46px; font-weight: 700; display: block; margin: 10px 0 8px; }
</style>
</head>
<body>
<main class="ad">
  <svg class="shapes" width="1200" height="1200" viewBox="0 0 1200 1200">
    <defs>
      <linearGradient id="photoTone" x1="0" y1="0" x2="1" y2="1">
        <stop offset="0" stop-color="#d9a891"/>
        <stop offset="0.5" stop-color="#e8bfae"/>
        <stop offset="1" stop-color="#c99584"/>
      </linearGradient>
    </defs>
    <!-- purple frame around photo blob -->
    <path d="M0,0 H710 C790,70 790,260 740,340 C695,410 600,425 520,445 C470,460 440,540 385,595 C330,640 250,640 180,600 C110,560 50,500 0,460 Z" fill="var(--purple)"/>
    <g role="img" aria-label="Close-up photo of a smiling mouth wearing metal braces">
      <path d="M0,0 H690 C765,80 760,260 712,330 C668,395 585,410 505,430 C455,445 425,520 375,570 C320,620 245,620 180,585 C110,545 50,490 0,470 Z" fill="url(#photoTone)"/>
    </g>
    <!-- left decorative pills -->
    <path d="M0,642 L48,630 A28,28 0 0 1 62,684 L0,700 Z" fill="var(--purple)"/>
    <path d="M0,724 L20,722 A26,26 0 0 1 24,796 L0,806 Z" fill="var(--purple)"/>
    <!-- bottom-right decorations -->
    <circle cx="1200" cy="1165" r="48" fill="var(--purple)"/>
    <path d="M1050,1200 C1070,1180 1110,1175 1140,1200 Z" fill="var(--purple)"/>
    <!-- date band -->
    <path d="M690,868 L712,866 L712,868 L1200,868 L1200,966 L664,966 Z" fill="none" stroke="#555" stroke-width="2"/>
    <path d="M712,858 L1200,858 L1200,955 L676,955 Z" fill="var(--purple)"/>
    <!-- offer band -->
    <path d="M240,998 L1093,998 L1050,1090 L240,1090 Z" fill="var(--purple)"/>
    <!-- badge -->
    <circle cx="158" cy="1044" r="122" fill="var(--white)" stroke="var(--purple)" stroke-width="1.5"/>
    <path d="M34,1044 A124,124 0 0 1 162,920" fill="none" stroke="var(--purple)" stroke-width="10"/>
    <circle cx="158" cy="1044" r="101" fill="var(--silver)"/>
    <circle cx="158" cy="1044" r="90" fill="var(--purple)"/>
  </svg>

  <div class="brand">
    <span class="brand-dot"></span>
    <span class="brand-name">RIDGELINE<small>FAMILY DENTISTRY · DR MAREN ELLSWORTH</small></span>
  </div>

  <h1 class="headline">
    <span class="accent">POST</span><br>
    <span class="dark">LOCKDOWN</span><br>
    <span class="accent">ORTHO SPECIAL</span>
  </h1>

  <div class="rule"></div>

  <p class="tagline">what better time to get<br><span class="hl">BRACES</span> when you have to wear a <span class="hl">MASK</span></p>

  <p class="date-text">July 31st 2020</p>

  <p class="offer-text">with free Consultation and Xrays</p>

  <p class="badge-text"><span class="small">Up to</span><span class="big">$2000</span><span class="small">off</span></p>
</main>
</body>
</html>
```